Lark Hollow Edibles product label

We are looking to create a product label for a new product. We are a THC edible company. Labels must not contain anything that resembles marijuana. Labels also must not contain anything that is appealing to children. The state is very strict. I want a professional label but also fun.

What the label must include.
Logo/Name (I will provide that in a file)
Dose: 50mg per pack
Servings: 10 servings per pack
Warning label for kids
Assorted flavors

Please be creative. Label size will need to be 3" wide and 5" tall.

```html
<!DOCTYPE html>
<html lang="en">
<head>
<meta charset="utf-8">
<title>Lark Hollow Edibles – THC Gummies Label</title>
<link href="https://fonts.googleapis.com/css2?family=Anton&family=Oswald:wght@400&family=Montserrat:wght@600;800&family=Quicksand:wght@400&family=Open+Sans:wght@400;700&display=swap" rel="stylesheet">
<style>
  :root{
    --backdrop:#a9c3d8;
    --label-white:#ffffff;
    --navy:#1f3f6c;
    --band-blue:#3a6088;
    --pink:#e0559f;
    --warn-red:#d8232a;
    --text-light:#ffffff;
  }
  *{box-sizing:border-box;margin:0;padding:0}
  html,body{width:1200px;height:1200px;overflow:hidden}
  body{background:var(--backdrop);position:relative}
  .label{
    position:absolute;left:210px;top:60px;width:780px;height:1080px;
    background:var(--label-white);overflow:hidden;
  }
  .fruit-photo{
    position:absolute;left:0;top:0;width:780px;height:880px;
    background:
      radial-gradient(circle at 12% 12%, #b3142a 0 9%, transparent 16%),
      radial-gradient(circle at 90% 6%, #c4253a 0 5%, transparent 10%),
      radial-gradient(circle at 88% 26%, #ef5b3f 0 11%, transparent 18%),
      radial-gradient(circle at 88% 50%, #e9738d 0 9%, transparent 15%),
      radial-gradient(circle at 14% 42%, #7a1025 0 8%, transparent 14%),
      radial-gradient(circle at 20% 62%, #e23a2e 0 12%, transparent 19%),
      radial-gradient(circle at 14% 80%, #1e1a24 0 7%, transparent 12%),
      radial-gradient(circle at 44% 80%, #95c24f 0 8%, transparent 14%),
      radial-gradient(circle at 86% 74%, #4d6a99 0 7%, transparent 12%),
      radial-gradient(circle at 60% 94%, #e2332a 0 10%, transparent 16%),
      #f6f2f0;
  }
  .banner{position:absolute;left:165px;top:0;width:450px;height:665px}
  .brand{
    position:absolute;left:0;width:100%;top:62px;
    display:flex;align-items:center;justify-content:center;gap:14px;
    font-family:"Montserrat",sans-serif;font-weight:600;font-size:30px;
    color:var(--text-light);letter-spacing:1px;
  }
  .brand-mark{width:34px;height:34px;background:var(--text-light)}
  .product-name{
    position:absolute;left:0;width:100%;top:160px;text-align:center;
    font-family:"Anton",sans-serif;font-size:170px;line-height:170px;
    color:var(--text-light);letter-spacing:2px;
  }
  .product-type{
    position:absolute;left:0;width:100%;top:330px;text-align:center;
    font-family:"Oswald",sans-serif;font-size:86px;line-height:100px;
    color:var(--text-light);letter-spacing:4px;
  }
  .flavor-tag{
    position:absolute;left:35px;width:382px;top:446px;height:57px;
    background:var(--pink);color:var(--text-light);
    font-family:"Quicksand",sans-serif;font-size:39px;line-height:57px;text-align:center;
  }
  .dose-info{
    position:absolute;left:0;width:780px;top:690px;text-align:center;
    font-family:"Montserrat",sans-serif;font-weight:800;color:var(--text-light);
    text-shadow:0 0 3px var(--navy),2px 2px 0 var(--navy),-2px -2px 0 var(--navy),2px -2px 0 var(--navy),-2px 2px 0 var(--navy);
  }
  .dose-info .servings{font-size:42px;line-height:62px}
  .dose-info .strength{font-size:58px;line-height:70px}
  .info-band{
    position:absolute;left:24px;right:24px;top:855px;bottom:0;
    background:var(--band-blue);
  }
  .kid-warning{
    position:absolute;left:33px;top:35px;width:155px;height:135px;
    background:var(--label-white);text-align:center;padding-top:10px;
    font-family:"Open Sans",sans-serif;color:#111;
  }
  .warn-icon{
    width:72px;height:66px;margin:0 auto;border:5px solid var(--warn-red);border-radius:8px;
    color:var(--warn-red);font-weight:700;font-size:44px;line-height:56px;
  }
  .warn-title{font-weight:700;font-size:15px;margin-top:8px}
  .warn-sub{font-weight:700;font-size:8.5px}
  .compliance{
    position:absolute;left:215px;right:20px;top:30px;color:var(--text-light);
    font-family:"Open Sans",sans-serif;
  }
  .compliance h2{font-weight:700;font-size:33px;line-height:42px}
  .compliance p{font-size:20px;line-height:30px}
</style>
</head>
<body>
  <main class="label">
    <div class="fruit-photo" role="img" aria-label="Photo of assorted fresh fruit: strawberries, raspberries, cherries, blueberries, blackberries and gooseberries"></div>

    <section class="banner">
      <svg width="450" height="665" viewBox="0 0 450 665">
        <polygon points="0,0 450,0 450,505 225,665 0,505" fill="var(--navy)"/>
        <polygon points="18,0 432,0 432,497 225,645 18,497" fill="none" stroke="#ffffff" stroke-width="3"/>
      </svg>
      <div class="brand"><span class="brand-mark"></span><span>Lark Hollow Edibles</span></div>
      <h1 class="product-name">THC</h1>
      <div class="product-type">GUMMIES</div>
      <div class="flavor-tag">Assorted flavors</div>
    </section>

    <div class="dose-info">
      <div class="servings">10 SERVINGS PER PACK</div>
      <div class="strength">50MG PER PACK</div>
    </div>

    <section class="info-band">
      <div class="kid-warning">
        <div class="warn-icon">!</div>
        <div class="warn-title">CONTAINS THC</div>
        <div class="warn-sub">NOT SAFE FOR KIDS OR PETS</div>
      </div>
      <div class="compliance">
        <h2>"Third party lab verified"</h2>
        <p>This gummy contains less than 0.3% Delta-9 THC and is federally legal in all 50 states according to the standards set forth in the 2018 Farm Bill.</p>
      </div>
    </section>
  </main>
</body>
</html>
```